Double-sided A5 leaflet with photos.

Design A5 leaflet double sided
With emphasis on we are cheaper than our competition as a hook
The colour can be whatever makes it look like a unique brand.
Try and use all the different photos because they are unique.
And put the different photos on there with headlines
Updates

Need extra days to review

Target Market(s)

The idea is it stands out people moving that you can offer different things to like taking their bed apart, taking their old furniture or they just want to move and want two men and the truck. Big or small or piano? Heavy furniture marble table? People who want their bed taken apart put back together again, piano moving, marble table. Moving fridge for washing machine. Moving small truck picture of big truck the poster is people walking past in the street. The orvek leaflet is delivered to high rise unit blocks with 300 units.

Industry/Entity Type

Furniture removal

Colors
59FF00
82FF00
B8FF75
E3FFCB
F4FFEA

Requirements
Must have
• Try and use all the different photos the screenshot of the Plindo review next to the other photos we put beds together, etc
Nice to have
• It would be nice to have on one side all the different photos with headlines on each one saying what they do EG beds taken apart over the top of a photo .g

```html
<!DOCTYPE html>
<html lang="en">
<head>
<meta charset="utf-8">
<title>Steady Movers – Leaflet</title>
<link rel="stylesheet" href="https://fonts.googleapis.com/css2?family=Poppins:wght@400;500;600;700;800&display=swap">
<style>
  :root {
    --navy: #12324f;
    --orange: #f5921e;
    --white: #ffffff;
    --ink: #0e1a26;
    --stage: #d1d3d5;
    --stamp: #e4e5e7;
    --rule: #9a9ea3;
    --leaf: #2f7a45;
  }
  * { margin: 0; padding: 0; box-sizing: border-box; }
  html, body { width: 1200px; height: 1200px; overflow: hidden; }
  body { background: var(--stage); font-family: "Poppins", sans-serif; position: relative; }

  .card { position: absolute; left: 180px; width: 841px; height: 396px; background: var(--white); overflow: hidden; }
  .card--front { top: 174px; }
  .card--back { top: 630px; }
  .card__bg { position: absolute; inset: 0; }

  /* Front */
  .headline { position: absolute; left: 14px; top: 12px; font-weight: 800; font-size: 41px; line-height: 47px; letter-spacing: -0.5px; }
  .headline__top { color: var(--orange); display: block; }
  .headline__bottom { color: var(--white); display: block; }
  .areas { position: absolute; left: 17px; top: 122px; color: var(--white); font-weight: 700; font-size: 13.5px; line-height: 19px; }
  .divider { position: absolute; left: 16px; top: 169px; width: 349px; height: 1px; background: #8ea0b2; }
  .features { position: absolute; left: 17px; top: 180px; list-style: none; }
  .features li { color: var(--white); font-size: 11px; line-height: 20.8px; display: flex; align-items: center; gap: 7px; }
  .features svg { width: 10px; height: 10px; flex: none; }

  .brand-mark { position: absolute; display: flex; align-items: center; gap: 6px; }
  .brand-mark__dot { width: 26px; height: 26px; border-radius: 50%; background: var(--leaf); flex: none; }
  .brand-mark__name { font-weight: 800; font-size: 13px; line-height: 14px; color: var(--white); text-transform: uppercase; }
  .card--front .brand-mark { left: 318px; top: 233px; }

  .contact { position: absolute; left: 0; top: 313px; width: 385px; text-align: center; }
  .contact__label { color: var(--white); font-weight: 700; font-size: 17px; line-height: 20px; }
  .contact__phone { color: var(--navy); font-weight: 800; font-size: 35px; line-height: 38px; letter-spacing: 0.5px; }
  .contact__web { color: var(--white); font-weight: 700; font-size: 16px; line-height: 18px; }

  .stamp { position: absolute; left: 721px; top: 17px; width: 83px; height: 83px; background: var(--stamp); }
  .address-line { position: absolute; left: 503px; width: 322px; height: 1px; background: var(--rule); }

  /* Back */
  .back .brand-mark, .card--back .brand-mark--lead { left: 14px; top: 50px; flex-direction: column; gap: 4px; width: 110px; text-align: center; }
  .card--back .brand-mark--lead .brand-mark__dot { width: 44px; height: 44px; }
  .card--back .brand-mark--lead .brand-mark__name { color: var(--navy); font-size: 12px; }

  .question { position: absolute; left: 127px; top: 30px; color: var(--ink); font-weight: 800; }
  .question__big { display: block; font-size: 34px; line-height: 38px; letter-spacing: -0.3px; }
  .question__small { display: block; font-size: 26px; line-height: 30px; }
  .compare { position: absolute; left: 127px; top: 119px; color: var(--ink); font-weight: 700; font-size: 21px; line-height: 26px; }

  .photo { position: absolute; left: 473px; top: 0; width: 368px; height: 396px;
    background: linear-gradient(160deg, #a9c4de 0%, #dfe6ec 28%, #2f7a45 42%, #e9ecee 62%, #7d8a6e 100%); }

  .rivals { position: absolute; left: 0; top: 182px; width: 500px; height: 106px; display: flex; }
  .rival { flex: 1; display: flex; align-items: center; justify-content: center; }
  .rival .brand-mark { position: static; flex-direction: column; gap: 5px; text-align: center; }
  .rival .brand-mark__dot { width: 40px; height: 40px; background: var(--navy); }
  .rival .brand-mark__name { color: var(--ink); font-size: 12px; }
  .rival--ours .brand-mark__dot { background: var(--leaf); }

  .prices { position: absolute; left: 0; top: 288px; width: 500px; height: 108px; display: flex; padding-top: 12px; }
  .price { flex: 1; text-align: center; color: var(--white); font-weight: 700; }
  .price__label { font-size: 11.5px; line-height: 15px; }
  .price__amount { color: var(--orange); font-weight: 800; font-size: 27px; line-height: 34px; }
  .price__note { font-size: 11.5px; line-height: 15px; }
</style>
</head>
<body>

<section class="card card--front" aria-label="Leaflet front">
  <svg class="card__bg" viewBox="0 0 841 396" width="841" height="396" aria-hidden="true">
    <polygon points="0,0 512,0 399,396 0,396" fill="var(--orange)"/>
    <polygon points="0,0 501,0 420,313 0,313" fill="var(--navy)"/>
  </svg>

  <h1 class="headline">
    <span class="headline__top">VERY VERY VERY</span>
    <span class="headline__bottom">CHEAP MOVERS!</span>
  </h1>
  <p class="areas">ALL AREAS OF SYDNEY.<br>FURNITURE REMOVALISTS AND REMOVALS.</p>
  <div class="divider"></div>

  <ul class="features">
    <li><svg viewBox="0 0 10 10"><rect x="0.6" y="0.6" width="8.8" height="8.8" fill="none" stroke="var(--orange)" stroke-width="1.2"/><path d="M2.2 5 L4.2 7 L8 2.6" fill="none" stroke="var(--orange)" stroke-width="1.4"/></svg>FLAT RATE $160 an hour for two men and a truck.</li>
    <li><svg viewBox="0 0 10 10"><rect x="0.6" y="0.6" width="8.8" height="8.8" fill="none" stroke="var(--orange)" stroke-width="1.2"/><path d="M2.2 5 L4.2 7 L8 2.6" fill="none" stroke="var(--orange)" stroke-width="1.4"/></svg>No extra charges compare to other quotes.</li>
    <li><svg viewBox="0 0 10 10"><rect x="0.6" y="0.6" width="8.8" height="8.8" fill="none" stroke="var(--orange)" stroke-width="1.2"/><path d="M2.2 5 L4.2 7 L8 2.6" fill="none" stroke="var(--orange)" stroke-width="1.4"/></svg>Units, houses office.</li>
    <li><svg viewBox="0 0 10 10"><rect x="0.6" y="0.6" width="8.8" height="8.8" fill="none" stroke="var(--orange)" stroke-width="1.2"/><path d="M2.2 5 L4.2 7 L8 2.6" fill="none" stroke="var(--orange)" stroke-width="1.4"/></svg>No extra for stairs.</li>
    <li><svg viewBox="0 0 10 10"><rect x="0.6" y="0.6" width="8.8" height="8.8" fill="none" stroke="var(--orange)" stroke-width="1.2"/><path d="M2.2 5 L4.2 7 L8 2.6" fill="none" stroke="var(--orange)" stroke-width="1.4"/></svg>No call out fee within the city area.</li>
    <li><svg viewBox="0 0 10 10"><rect x="0.6" y="0.6" width="8.8" height="8.8" fill="none" stroke="var(--orange)" stroke-width="1.2"/><path d="M2.2 5 L4.2 7 L8 2.6" fill="none" stroke="var(--orange)" stroke-width="1.4"/></svg>No base to base charge.</li>
  </ul>

  <div class="brand-mark">
    <span class="brand-mark__dot"></span>
    <span class="brand-mark__name">Steady<br>Movers</span>
  </div>

  <div class="contact">
    <p class="contact__label">CONTACT US</p>
    <p class="contact__phone">0400 555 019</p>
    <p class="contact__web">www.steadymovers.com.au</p>
  </div>

  <div class="stamp"></div>
  <div class="address-line" style="top:211px"></div>
  <div class="address-line" style="top:268px"></div>
  <div class="address-line" style="top:323px"></div>
</section>

<section class="card card--back" aria-label="Leaflet back">
  <div class="photo" role="img" aria-label="Photo of the company's white box truck with green branded body parked on a street"></div>
  <svg class="card__bg" viewBox="0 0 841 396" width="841" height="396" aria-hidden="true">
    <rect x="0" y="0" width="465" height="159" fill="var(--orange)"/>
    <path d="M0 151 H480 Q508 151 508 179 V396 H0 Z" fill="var(--white)"/>
    <path d="M0 159 H476 Q500 159 500 183 V182 H0 Z" fill="var(--navy)"/>
    <rect x="0" y="288" width="500" height="108" fill="var(--navy)"/>
  </svg>

  <div class="brand-mark brand-mark--lead">
    <span class="brand-mark__dot"></span>
    <span class="brand-mark__name">Steady Movers</span>
  </div>

  <h2 class="question">
    <span class="question__big">HOW MUCH COST</span>
    <span class="question__small">WILL TAKE MY MOVE?</span>
  </h2>
  <p class="compare">COMPARE QUOTES</p>

  <div class="rivals">
    <div class="rival"><div class="brand-mark"><span class="brand-mark__dot"></span><span class="brand-mark__name">Duo Haulage</span></div></div>
    <div class="rival"><div class="brand-mark"><span class="brand-mark__dot"></span><span class="brand-mark__name">Solo Van Co</span></div></div>
    <div class="rival rival--ours"><div class="brand-mark"><span class="brand-mark__dot"></span><span class="brand-mark__name">Steady Movers</span></div></div>
  </div>

  <div class="prices">
    <div class="price">
      <p class="price__label">1ST HOUR</p>
      <p class="price__amount">$465</p>
      <p class="price__note">THEN $250<br>PER HOUR</p>
    </div>
    <div class="price">
      <p class="price__label">PER HOUR</p>
      <p class="price__amount">$225</p>
      <p class="price__note">BASE TO BASE<br>FROM BROOKVALE</p>
    </div>
    <div class="price">
      <p class="price__label">PER HOUR</p>
      <p class="price__amount">$170</p>
      <p class="price__note">NO BASE TO BASE<br>CHARGE</p>
    </div>
  </div>
</section>

</body>
</html>
```